Minimalist- A clean spacious and crisp design for a Security Consulting Company

I need a design for a security consultant that deals with the upper end of town for security design, including CCTV and other electronic design. I need it to look spacious and be very simplistic in design. I want to keep it looking like Vantro or QUIBA's website. I have experience in business intelligence. and have a lot of high end clients in the diamond industry and mining. My key area of income is consulting and taking them from normal to excellent security.
Target Market(s)
People interested in doing business with me
Industry/Entity Type
Electronic
Coding
Coded - Design and coding required
Number of Pages Required
4 page
Requirements
Must have
- The least amount of text possible
- A simple and nice front page with the logo.
- A contact us button
- Specialised projects button
- About us button
- Business intelligence button
Should not have
- Cluttered un-useful information

```html
<!DOCTYPE html>
<html lang="en">
<head>
<meta charset="utf-8">
<title>Halden Strategy</title>
<link href="https://fonts.googleapis.com/css2?family=Open+Sans:ital,wght@0,300;0,400;0,600;0,700;1,400&display=swap" rel="stylesheet">
<style>
:root{
  --red:#a30c0c;
  --ink:#111;
  --grey-text:#777;
  --band:#ebebeb;
  --line:#d6d6d6;
  --footer:#000;
  --footer-text:#8a8a8a;
  --footer-head:#fff;
}
*{margin:0;padding:0;box-sizing:border-box}
html,body{width:1200px;height:2296px;overflow:hidden}
body{font-family:"Open Sans",Arial,sans-serif;background:#fff;color:var(--ink);position:relative}
.abs{position:absolute}
/* header */
.site-header{position:absolute;left:0;top:0;width:1200px;height:120px;background:#fff}
.brand{left:165px;top:38px;display:flex;align-items:center;gap:10px}
.brand-mark{width:34px;height:34px;background:var(--red)}
.brand-name{font-size:30px;font-weight:700;color:#222;letter-spacing:-.5px}
.main-nav{left:517px;top:48px;display:flex;align-items:center;gap:30px;font-size:13px;color:#333}
.main-nav .active{background:var(--red);color:#fff;padding:6px 20px;border-radius:3px}
/* hero */
.hero{left:0;top:120px;width:1200px;height:436px;background:linear-gradient(100deg,#7a3a2a 0%,#5a3328 38%,#2d3e60 60%,#1d2c4e 100%)}
.hero-title{left:175px;top:258px;font-size:31px;font-weight:400;color:#fff;line-height:54px;letter-spacing:.3px}
.pill{display:inline-flex;align-items:center;justify-content:center;border-radius:28px;color:#fff;font-size:14px}
.hero-btn{left:175px;top:382px;width:198px;height:54px;background:var(--red);text-transform:uppercase}
.dots{display:flex;gap:9px}
.dot{width:11px;height:11px;border-radius:50%;background:#bbb}
.dot.on{background:#fff}
/* welcome */
.section-title{width:1200px;left:0;text-align:center;font-size:31px;font-weight:700}
.welcome-text{left:180px;top:674px;width:840px;text-align:center;font-size:12.5px;line-height:33px;color:var(--grey-text)}
/* difference band */
.band{left:0;top:852px;width:1200px;height:293px;background:var(--band)}
.band-title{left:162px;top:882px;font-size:23px;font-weight:600}
.feature-list{left:182px;top:924px;list-style:none;font-size:12.5px;color:#444}
.feature-list li{height:27px;line-height:27px;display:flex;align-items:center;gap:12px}
.feature-list li::before{content:"";width:8px;height:8px;background:#888;transform:rotate(45deg)}
.band-btn{left:178px;top:1070px;width:152px;height:50px;background:#000}
/* services */
.service{width:300px;text-align:center}
.service-icon{width:90px;height:90px;border:1px solid var(--line);margin:0 auto;display:flex;align-items:center;justify-content:center;background:#fff}
.service h3{margin-top:28px;font-size:16px;font-weight:600}
.service p{margin-top:15px;font-size:12.5px;line-height:27px;color:var(--grey-text)}
/* testimonial */
.testimonial{left:0;top:1585px;width:1200px;height:348px;background:linear-gradient(180deg,#3a3532,#2c2826 60%,#201d1c)}
.portrait{left:192px;top:1634px;width:194px;height:196px;border-radius:6px;background:linear-gradient(160deg,#e6e2dc,#c9b8a6 55%,#2a3f6e)}
.quote-name{left:192px;top:1843px;width:194px;text-align:center;color:#fff;font-size:14px;font-weight:700}
.quote-role{left:192px;top:1867px;width:194px;text-align:center;color:#fff;font-size:12px;font-style:italic}
.quote-text{left:427px;top:1702px;width:600px;font-size:12.5px;line-height:27px;font-style:italic;color:#fff}
/* footer */
.site-footer{left:0;top:1933px;width:1200px;height:363px;background:var(--footer)}
.footer-col h4{color:var(--footer-head);font-size:17px;font-weight:600;margin-bottom:20px}
.footer-col a{display:block;color:var(--footer-text);font-size:12.5px;line-height:26.5px;text-decoration:none}
.to-top{left:1095px;top:2045px;width:50px;height:50px;background:#2a2a2a;display:flex;align-items:center;justify-content:center}
.rule{left:0;width:1200px;height:1px;background:#222}
.social{left:161px;top:2201px;display:flex;gap:22px;font-size:12px;color:var(--footer-text)}
.social span{display:flex;align-items:center;gap:8px}
.social i{width:16px;height:16px;background:#555;display:inline-block}
.legal{left:830px;top:2201px;display:flex;gap:26px;font-size:12px;color:var(--footer-text)}
.copyright{left:161px;top:2253px;font-size:12px;color:#555}
.build{left:1120px;top:2253px;font-size:12px;color:#555}
</style>
</head>
<body>
<header class="site-header">
  <div class="abs brand"><span class="brand-mark"></span><span class="brand-name">Halden Strategy</span></div>
  <nav class="abs main-nav">
    <span class="active">Home</span><span>About us</span><span>Specialised Projects</span><span>Business Intelligence</span><span>Contact us</span>
  </nav>
</header>

<section class="abs hero" role="img" aria-label="Photo of a security camera mounted on a brick wall against a dusk sky"></section>
<svg class="abs" style="left:44px;top:295px" width="30" height="88" viewBox="0 0 30 88"><polyline points="28,2 2,44 28,86" fill="none" stroke="#fff" stroke-width="1.5"/></svg>
<svg class="abs" style="left:1126px;top:295px" width="30" height="88" viewBox="0 0 30 88"><polyline points="2,2 28,44 2,86" fill="none" stroke="#fff" stroke-width="1.5"/></svg>
<h1 class="abs hero-title">EVERYTHING YOU NEED TO RUN YOUR<br>BUSINESS, BEAUTIFULLY...</h1>
<a class="abs pill hero-btn">Specialised Projects</a>
<div class="abs dots" style="left:573px;top:528px"><span class="dot"></span><span class="dot on"></span><span class="dot"></span></div>

<h2 class="abs section-title" style="top:596px">Welcome to Halden Strategy</h2>
<p class="abs welcome-text">Lorem Ipsum is simply dummy text of the printing and typesetting industry. Lorem Ipsum has been the industry's standard dummy text ever since the 1500s, when an unknown printer took a galley of type and scrambled it to make a type specimen book. It has survived not only five centuries, but also the leap into electronic typesetting, remaining essentially unchanged. It was popularised in the 1960s with the release of Typeline sheets containing Lorem Ipsum passages, and more recently with desktop publishing software like Inkset Composer including versions of Lorem Ipsum.</p>

<section class="abs band"></section>
<svg class="abs" style="left:660px;top:852px" width="540" height="293" viewBox="0 0 540 293" role="img" aria-label="Photo of a technician installing a security camera on a wall"><defs><linearGradient id="installGrad" x1="0" y1="0" x2="1" y2="1"><stop offset="0" stop-color="#d8d6d2"/><stop offset=".55" stop-color="#8f8d8a"/><stop offset="1" stop-color="#3e3b39"/></linearGradient></defs><polygon points="190,0 540,0 540,293 0,293" fill="url(#installGrad)"/></svg>
<h2 class="abs band-title">We build the difference and they will want it.</h2>
<ul class="abs feature-list"><li>Business Process</li><li>SWOT</li><li>Strategy</li><li>Office Technology</li><li>Governance Clients</li></ul>
<a class="abs pill band-btn">VIEW MORE</a>

<h2 class="abs section-title" style="top:1177px">Our Services</h2>
<div class="abs service" style="left:150px;top:1278px">
  <div class="service-icon"><svg width="58" height="58" viewBox="0 0 58 58"><rect x="2" y="36" width="12" height="20" fill="#999"/><rect x="20" y="24" width="12" height="32" fill="#999"/><rect x="38" y="10" width="12" height="46" fill="#999"/></svg></div>
  <h3>Business Process</h3>
  <p>Lorem Ipsum is simply dummy text of the printing and typesetting industry. Lorem Ipsum has been the industry's standard dummy.</p>
</div>
<div class="abs service" style="left:450px;top:1278px">
  <div class="service-icon"><svg width="50" height="58" viewBox="0 0 50 58"><path d="M8 42 L25 4 L42 42 M14 29 H36" fill="none" stroke="#999" stroke-width="4"/><rect x="3" y="48" width="44" height="6" fill="#999"/></svg></div>
  <h3>Charter</h3>
  <p>Lorem Ipsum is simply dummy text of the printing and typesetting industry. Lorem Ipsum has been the industry's standard dummy.</p>
</div>
<div class="abs service" style="left:750px;top:1278px">
  <div class="service-icon"><svg width="50" height="52" viewBox="0 0 50 52"><circle cx="25" cy="15" r="12" fill="#999"/><path d="M3 50 Q5 30 25 30 Q45 30 47 50 Z" fill="#999"/></svg></div>
  <h3>Professional Services</h3>
  <p>Lorem Ipsum is simply dummy text of the printing and typesetting industry. Lorem Ipsum has been the industry's standard dummy.</p>
</div>

<section class="abs testimonial" role="img" aria-label="Dimmed photo of a team working together around an office table"></section>
<div class="abs portrait" role="img" aria-label="Portrait photo of the client giving the testimonial"></div>
<p class="abs quote-name">Miss. Dana Whitford</p>
<p class="abs quote-role">CEO, Company Name</p>
<p class="abs quote-text">Lorem Ipsum is simply dummy text of the printing and typesetting industry. Lorem Ipsum has been the industry's standard dummy text ever since the 1500s, when an unknown printer took a galley of type and scrambled it to make a type specimen book. It has survived not only five centuries, but also the leap into electronic typesetting, remaining essentially unchanged.</p>
<div class="abs dots" style="left:573px;top:1897px"><span class="dot"></span><span class="dot on"></span><span class="dot"></span></div>

<footer class="abs site-footer"></footer>
<div class="abs footer-col" style="left:161px;top:1956px"><h4>Partners</h4><a>Accountants</a><a>Bookkeepers</a><a>Products</a><a>Education &amp; training</a><a>Partner program</a><a>Accountant &amp; Bookkeeper Guides</a></div>
<div class="abs footer-col" style="left:485px;top:1956px"><h4>More resources</h4><a>Add-on Marketplace</a><a>Videos &amp; guides – QUIBA TV</a><a>Training &amp; events – QUIBA U</a><a>Developer tools</a><a>Blog</a></div>
<div class="abs footer-col" style="left:827px;top:1956px"><h4>Contact &amp; info</h4><a>About us</a><a>Media</a><a>Investors</a><a>Careers</a><a>Support</a><a>Contact us</a></div>
<div class="abs to-top"><svg width="24" height="16" viewBox="0 0 24 16"><polyline points="2,14 12,3 22,14" fill="none" stroke="#fff" stroke-width="3"/></svg></div>
<div class="abs rule" style="top:2188px"></div>
<div class="abs social"><span><i></i>Facenote</span><span><i></i>Chirper</span><span><i></i>Circles</span></div>
<div class="abs legal"><span>Terms of use</span><span>Site map</span><span>Privacy</span></div>
<div class="abs rule" style="top:2236px"></div>
<p class="abs copyright">© 2015 HaldenStrategy.com</p>
<p class="abs build">C20</p>
</body>
</html>
```